Kettlelanternpress: Self-help book needs Promotional Postcard

Need a postcard 8.5" x 5.5" to promote my upcoming book. Its a self-help career book for women focusing on how the mother-daughter relationship impacts careers and tips and solutions for success. The model includes 5 different types of daughters.
Title: Where Did the Quiet Garden Lead Us?
Breathe new life into your career by understanding your mother daughter relationship.
Book release is January 9, 2017
Updates

I just uploaded 5 images of the daughter types without the words, better to use these, thanks! Added Thursday, December 29, 2016

Target Market(s)

This book is targeted towards women

Industry/Entity Type

Promotional

Font styles to use
Serif
Other font styles liked:
• see website text

Colors
00a990
ec252d
e34297

Requirements
Must have
• Eye catching promotional postcard. Must have image of book on front with title and subtitle, author name and website. I'd like images of the 5 daughters on the front.
• Colors should match the cover green and pink
• Back can have quotes and author bio
• can look at website (not quite completed) for more inspiration www.kettlelanternpress.example
Nice to have
• Curious to see how the postcard compliments the book and website.

```html
<!DOCTYPE html>
<html lang="en">
<head>
<meta charset="utf-8">
<title>Where Did the Quiet Garden Lead Us? – Postcard</title>
<link rel="stylesheet" href="https://fonts.googleapis.com/css2?family=Montserrat:wght@300;400;500;600;700&display=swap">
<style>
  :root{
    --backdrop:#f9c27f;
    --magenta:#a81d4f;
    --olive:#2f3527;
    --cover-green:#7c8c55;
    --gold:#f6a623;
    --title-yellow:#f3b64b;
    --ink:#1d1d1d;
    --white:#ffffff;
  }
  *{margin:0;padding:0;box-sizing:border-box}
  html,body{width:900px;height:1200px;overflow:hidden}
  body{background:var(--backdrop);font-family:"Montserrat",Arial,sans-serif;color:var(--ink);position:relative}

  .card{position:absolute;left:42px;width:816px;background:var(--white);box-shadow:2px 3px 6px rgba(0,0,0,.25);overflow:hidden}
  .card--front{top:52px;height:528px}
  .card--back{top:604px;height:526px}

  /* front */
  .hero-photo{position:absolute;left:400px;top:0;width:416px;height:528px;
    background:radial-gradient(ellipse at 60% 45%,#bdbdbd 0%,#a0a0a0 35%,#e4e4e4 70%,#fafafa 100%);}
  .tile{position:absolute;border:3px solid var(--white)}
  .tile--pink{background:var(--magenta)}
  .tile--olive{background:var(--olive)}
  .wave{position:absolute;left:0;top:0}
  .site-link{position:absolute;left:64px;top:280px;font-weight:700;font-size:12.5px;letter-spacing:.2px;z-index:2}
  .book-cover{position:absolute;left:298px;top:233px;width:145px;height:179px;background:var(--cover-green);
    text-align:center;color:var(--magenta);padding-top:12px;box-shadow:1px 1px 3px rgba(0,0,0,.3);z-index:2}
  .book-cover__title{font-weight:500;font-size:13px;line-height:1.15;letter-spacing:2px;color:var(--magenta)}
  .book-cover__title b{font-size:26px;font-weight:600;letter-spacing:1px;display:block;line-height:1.1}
  .book-cover__sub{font-size:5.5px;color:var(--olive);margin-top:8px;line-height:1.3}
  .book-cover__author{font-size:7px;margin-top:8px}
  .front-copy{position:absolute;left:34px;top:396px;color:var(--white);z-index:2}
  .front-copy__author{font-size:20px;font-weight:300;color:var(--title-yellow)}
  .front-copy__title{font-size:25px;font-weight:700;margin-top:6px}
  .front-copy__sub{font-size:16px;font-weight:300;line-height:22px;margin-top:4px}
  .release-badge{position:absolute;left:668px;top:392px;width:200px;height:200px;border-radius:50%;
    background:var(--gold);border:2px solid var(--white);box-shadow:0 0 0 2px #222;z-index:3}
  .release-badge__text{position:absolute;left:22px;top:52px;transform:rotate(-28deg);font-weight:700;
    color:var(--ink);font-size:17px;line-height:22px;text-align:center;width:140px}
  .release-badge__text span{font-weight:300}

  /* back */
  .back-left{position:absolute;left:0;top:0;width:418px;height:456px;padding:32px 24px 0 26px}
  .back-right{position:absolute;left:418px;top:0;width:398px;height:456px;padding:30px 24px 0 28px;
    background:linear-gradient(160deg,#f2f2f2 0%,#e1e1e1 50%,#f4f4f4 100%)}
  .section-title{font-weight:600;font-size:16px;margin-bottom:6px}
  .body-copy{font-size:11.4px;line-height:15.5px;text-align:justify}
  .type-row{display:flex;gap:6px;margin:28px 0 0 75px}
  .type-row .mini{width:40px;height:40px}
  .author-block{margin-top:20px}
  .author-photo{float:left;width:76px;height:76px;border-radius:50%;margin:0 10px 0 0;
    shape-outside:inset(0 0 8px 0);height:76px;
    background:radial-gradient(circle at 50% 45%,#c49a6a,#7f5e3d);border:3px solid #bdbdbd}
  .author-block .section-title{padding-top:16px;margin-bottom:4px}
  .author-block .body-copy{clear:none}
  .quote{color:var(--magenta);font-size:11.6px;line-height:15.5px;margin-bottom:18px;hyphens:auto;-webkit-hyphens:auto}
  .quote-name{font-weight:700;font-size:13px;line-height:14px}
  .quote-role{font-size:7.5px;line-height:10px;margin-bottom:18px}
  .contact-band{position:absolute;left:0;top:456px;width:816px;height:70px;background:var(--magenta);
    color:var(--white);font-weight:600;font-size:13px;line-height:17px;text-align:center;padding-top:18px}
  .contact-band em{font-style:normal;color:var(--title-yellow)}
</style>
</head>
<body>

<section class="card card--front">
  <div class="hero-photo" role="img" aria-label="Black and white photo of a smiling adult daughter embracing her mother"></div>

  <div class="tile tile--pink" style="left:34px;top:21px;width:86px;height:82px" role="img" aria-label="Daughter type silhouette, wavy hair"></div>
  <div class="tile tile--pink" style="left:11px;top:102px;width:126px;height:114px" role="img" aria-label="Daughter type silhouette, long straight hair"></div>
  <div class="tile tile--olive" style="left:122px;top:61px;width:118px;height:110px" role="img" aria-label="Daughter type silhouette, curly hair"></div>
  <div class="tile tile--pink" style="left:240px;top:60px;width:120px;height:110px" role="img" aria-label="Daughter type silhouette, ponytail"></div>
  <div class="tile tile--olive" style="left:136px;top:171px;width:104px;height:96px" role="img" aria-label="Daughter type silhouette, short bob"></div>

  <svg class="wave" width="816" height="528" viewBox="0 0 816 528" aria-hidden="true">
    <path d="M0 378 C80 374 150 374 212 362 C236 308 290 284 335 286 C378 270 432 282 462 310 C500 332 530 362 552 402 L600 528 L0 528 Z" fill="var(--magenta)"/>
  </svg>

  <div class="site-link">www.kettlelanternpress.example</div>

  <div class="book-cover">
    <div class="book-cover__title">WHERE DID THE<br>QUIET<b>GARDEN</b>LEAD US?</div>
    <div class="book-cover__sub">Breathe New Life Into Your Career<br>by Understanding Your<br>Mother-Daughter Relationship</div>
    <div class="book-cover__author">Mara Quill Densmore, M.A, M.Ed</div>
  </div>

  <div class="front-copy">
    <div class="front-copy__author">Mara Quill Densmore's</div>
    <div class="front-copy__title">Where Did the Quiet Garden Lead Us?</div>
    <div class="front-copy__sub">Breathe new life into your career<br>by understanding your mother daughter relationship.</div>
  </div>

  <div class="release-badge">
    <div class="release-badge__text">BOOK RELEASE<br><span>9<sup>TH</sup> JANUARY</span><br>2017</div>
  </div>
</section>

<section class="card card--back">
  <div class="back-left">
    <h2 class="section-title">About the Book</h2>
    <p class="body-copy">Are you unhappy at work? Feeling uncertain about your career choices in general? Your relationship with your mother might be the last thing on your mind as a major contributing factor to your career woes but it shouldn't be. Unlock the mystery to the patterns and choices you make throughout your career. Read about the five daughter types, and learn how to propel your career forward.</p>

    <div class="type-row">
      <div class="mini tile--pink" role="img" aria-label="Daughter type silhouette"></div>
      <div class="mini tile--olive" role="img" aria-label="Daughter type silhouette"></div>
      <div class="mini tile--pink" role="img" aria-label="Daughter type silhouette"></div>
      <div class="mini tile--olive" role="img" aria-label="Daughter type silhouette"></div>
      <div class="mini tile--pink" role="img" aria-label="Daughter type silhouette"></div>
    </div>

    <div class="author-block">
      <div class="author-photo" role="img" aria-label="Portrait photo of the author"></div>
      <h2 class="section-title">About the Authour</h2>
      <p class="body-copy"><b>Mara Quill Densmore</b>, M.A., M.Ed. is a clinical career counselor and licensed mental health counselor who has been helping clients make meaningful career transitions and address workplace challenges for over 26 years. She is the 2013 recipient of the Outstanding Career Practitioner Award from the Regional Career Guidance Guild. ‘Quiet Garden’ integrates her expertise in career development with her training and insight about the adult mother-daughter relationship.</p>
    </div>
  </div>

  <div class="back-right" role="img" aria-label="Faded photo of mother and daughter behind the reviews">
    <p class="quote">"...Mara draws the reader in with her poignant &amp; insightful perspective of how family dynamics, particularly the conscious &amp; subconscious aspects of the mother/daughter relationship, impact a career path and a fulfilled life..."</p>
    <p class="quote-name">Judge Renata Calloway,</p>
    <p class="quote-role">COURT HOUR, a syndicated TV court program.</p>

    <p class="quote">"...Putting the not so obvious 2 + 2 together (mothers + careers) gives all women a chance to stand up in their own truth, letting go of old messages (conscious &amp; unconscious) that still define them, even in the workplace. a great "how to" book, with tips that will serve you well, no matter which daughter type you might be..."</p>
    <p class="quote-name">Dr. Helena Marsh,</p>
    <p class="quote-role">Co-author with her mother of Mothers &amp; Daughters: Finding the Way and other books<br>including: Warm Bread for the Mother &amp; Daughter Heart..</p>

    <p class="quote">"...'Quiet Garden' challenges us to pay attention to how we show up at work without assigning blame or judgement. Mara draws on decades of career counseling to provide knowledgeable insight and practical tips, wrapped in a warm hug..."</p>
    <p class="quote-name">Tessa J Rowan,</p>
    <p class="quote-role">Executive Women's Leadership and Mindfulness Coach.</p>
  </div>

  <div class="contact-band">
    To Book Mara for a speaking event, please contact her at <em>555 014-2287</em><br>
    or visit <em>www.kettlelanternpress.example</em> for more information.
  </div>
</section>

</body>
</html>
```